Renewable Energy company needs a new website

We are renewable energy company that has been operating for 3 years now and require a new website design. We are looking to upgrade our website to be comparable to our competitors. We are not a brick and mortar business so our website does need to be very appealing and convey a sense of authenticity and trust to the consumer. It will also heavily display our current system special and offering etc. The final design needs to be visually appealing in a marketing sense however also needs to convey a high sense of professionalism.

Target Market(s)

Consumers of solar systems for installation on their home or business.

Coding

Coded - Design and coding required

Number of Pages Required

3 page

Font styles to use
Sans Serif

Colors

Designer to choose colors to be used in the design.

Requirements
Must have
• A home page, a page for residential solar systems including the packages we are currently offering and a commercial page for larger installations of solar systems.
• www.torvapower.com.au
Nice to have
• As a template we do like this https://www.bluneklight.com.au/qld/ in terms of design elements and layout of the page.

```html
<!DOCTYPE html>
<html lang="en">
<head>
<meta charset="utf-8">
<title>Torva Power – Solar &amp; Off-Grid Energy</title>
<link href="https://fonts.googleapis.com/css2?family=Oswald:wght@400;500;600&family=Roboto:ital,wght@0,400;0,500;0,700;1,400&display=swap" rel="stylesheet">
<style>
:root{
  --red:#c51f2e;
  --red-dark:#a9141f;
  --ink:#222;
  --text:#555;
  --muted:#8a8a8a;
  --line:#e4e4e4;
  --yellow:#f7d11b;
  --footer:#1f2229;
  --panel:#ececec;
}
*{box-sizing:border-box;margin:0;padding:0}
html,body{width:1200px;height:4518px;overflow:hidden}
body{font-family:'Roboto',sans-serif;color:var(--text);background:#fff;position:relative}
.abs{position:absolute}
.head{font-family:'Oswald',sans-serif;font-weight:500;color:var(--ink);text-transform:uppercase;letter-spacing:.3px}

/* top bar */
.topbar{top:0;left:0;width:1200px;height:32px;border-bottom:1px solid var(--line);font-size:11px;color:var(--muted)}
.topbar .lang{left:140px;top:9px}
.topbar .socials{right:90px;top:0;display:flex}
.topbar .socials span{width:44px;height:32px;border-left:1px solid var(--line);display:flex;align-items:center;justify-content:center}
.topbar .socials i{width:8px;height:8px;border-radius:50%;background:#aaa;display:block}

/* nav */
.nav{top:32px;left:0;width:1200px;height:96px;border-bottom:1px solid var(--line)}
.brand{left:92px;top:22px;display:flex;align-items:center;gap:8px}
.brand .mark{width:34px;height:34px;background:var(--red)}
.brand .name{font-family:'Oswald',sans-serif;font-weight:600;font-size:24px;color:var(--red);line-height:1}
.menu{left:282px;top:43px;display:flex;gap:28px;font-size:13px;font-weight:500;color:#333}
.cart{left:822px;top:42px}
.search{left:893px;top:43px}
.quote-btn{left:947px;top:29px;width:161px;height:43px;background:var(--red);color:#fff;font-size:12px;font-weight:700;letter-spacing:1px;display:flex;align-items:center;justify-content:center}

/* hero */
.hero{top:128px;left:0;width:1200px;height:614px;background:linear-gradient(100deg,#0f2345 0%,#1d3f73 45%,#5a86c4 75%,#9bb9e0 100%)}
.hero h1{left:96px;top:196px;font-family:'Oswald',sans-serif;font-weight:600;font-size:54px;line-height:66px;color:#fff;text-transform:uppercase}
.hero p{left:96px;top:340px;width:590px;font-size:13.5px;line-height:22px;color:#fff}
.hero .cta{left:96px;top:425px;width:177px;height:40px;background:#fff;color:#333;font-size:13px;display:flex;align-items:center;justify-content:center}

/* service cards */
.card{top:812px;width:236px;height:272px;background:#fff;box-shadow:0 4px 16px rgba(0,0,0,.12)}
.card svg{position:absolute;left:26px;top:38px}
.card .tag{position:absolute;left:26px;top:154px;font-size:12px;color:#444;text-transform:uppercase}
.card .title{position:absolute;left:26px;top:180px;width:200px;font-size:20px;line-height:31px;color:#333}
.card.active{background:var(--red)}
.card.active .tag,.card.active .title{color:#fff}

/* intro + form */
.intro h2{left:88px;top:1164px;font-size:44px;line-height:52px;width:600px}
.intro p{left:90px;width:580px;font-size:13.5px;line-height:22px;color:var(--muted)}
.illus{left:150px;top:1400px;width:480px;height:440px;background:radial-gradient(ellipse at 50% 55%,#d7dde6 0%,#eef1f5 55%,#fff 75%)}
.form{left:752px;top:1177px;width:357px;height:645px;background:#fff;box-shadow:0 3px 14px rgba(0,0,0,.14)}
.form h3{position:absolute;top:38px;width:100%;text-align:center;font-family:'Oswald',sans-serif;font-weight:500;font-size:18px;color:#222}
.form .sub{position:absolute;top:68px;left:40px;width:277px;text-align:center;font-family:'Oswald',sans-serif;font-size:12px;line-height:22px;color:#444}
.form .field{position:absolute;left:36px;width:285px;height:44px;border:1px solid #d8d8d8;font-family:'Oswald',sans-serif;font-size:12px;color:#888;padding:13px 18px}
.form .field.sel{color:#333}
.form .submit{position:absolute;left:36px;top:524px;width:285px;height:44px;background:var(--red);color:#fff;font-family:'Oswald',sans-serif;font-size:13px;display:flex;align-items:center;justify-content:center}

/* products */
.section-title{width:1200px;left:0;text-align:center}
.prod{top:1982px;width:236px}
.prod .img{height:272px;background:var(--panel)}
.prod .img div{position:absolute;left:40px;top:50px;width:156px;height:150px;background:linear-gradient(150deg,#7fb2ea,#2b4f8a);opacity:.55}
.prod .name{margin-top:22px;font-family:'Oswald',sans-serif;font-weight:500;font-size:21px;color:#222}
.prod .price{font-family:'Oswald',sans-serif;font-weight:500;font-size:34px;line-height:40px;color:var(--red)}
.prod .btn{margin-top:14px;width:128px;height:38px;background:var(--yellow);color:#222;font-size:11px;font-weight:500;display:flex;align-items:center;justify-content:center}

/* why solar */
.why{top:2478px;left:0;width:1200px;height:658px;background:linear-gradient(180deg,#cc2f3d,#c42634)}
.why h2{top:2560px;color:#fff;font-size:42px}
.tabs{top:2628px;left:80px;width:1040px;display:flex;justify-content:space-between;font-size:11px;color:#fff}
.tab-line{top:2656px;left:80px;width:172px;height:2px;background:#fff}
.why h3{left:88px;top:2750px;font-size:21px;color:#fff}
.why p{left:90px;width:520px;font-size:13.5px;line-height:22px;color:#fff;text-align:justify}
.why .photo{left:666px;top:2670px;width:360px;height:400px;border-radius:50%;background:radial-gradient(circle at 50% 25%,#f3c98a 0%,#b98a6a 30%,#3e4f7a 65%,#23335c 100%);box-shadow:14px 8px 0 #a7121d}

/* grow */
.grow h2{top:3215px;font-size:42px;line-height:50px}
.story{top:3354px}
.story .img{width:214px;height:219px;background:linear-gradient(180deg,#e2b98a,#5a6f99 60%,#2e3e6b)}
.story h4{position:absolute;left:240px;top:16px;width:280px;font-family:'Oswald',sans-serif;font-weight:500;font-size:15px;line-height:22px;color:#222;text-transform:uppercase}
.story p{position:absolute;left:242px;top:72px;width:262px;font-size:13px;line-height:22px;color:#555;text-align:justify}
.story .btn{position:absolute;left:242px;top:163px;width:128px;height:40px;background:var(--red);color:#fff;font-size:11px;display:flex;align-items:center;justify-content:center}

/* testimonials */
.testis h2{top:3680px;font-size:42px}
.testi{top:3800px}
.testi .avatar{width:128px;height:128px;border-radius:50%;background:#d9dce2;border:5px solid #fff;box-shadow:0 3px 14px rgba(0,0,0,.18)}
.testi .quote{position:absolute;left:154px;top:-24px;font-family:'Oswald',sans-serif;font-size:180px;line-height:1;color:#eee}
.testi p{position:absolute;left:150px;top:30px;width:300px;font-style:italic;font-size:13.5px;line-height:28px;color:#777}
.testi .who{position:absolute;left:150px;top:106px;font-style:italic;font-size:15px;color:#444}

/* footer */
.footer{top:4040px;left:0;width:1200px;height:478px;background:var(--footer);color:#fff}
.footer .f-brand{left:80px;top:62px;display:flex;align-items:center;gap:8px}
.footer .f-brand .mark{width:30px;height:30px;background:var(--red)}
.footer .f-brand .name{font-family:'Oswald',sans-serif;font-weight:600;font-size:22px;color:#fff}
.footer .txt{font-size:13px;line-height:20px;color:#fff}
.footer h5{font-size:14px;font-weight:500;letter-spacing:.5px}
.footer .bar{width:40px;height:2px;background:var(--red)}
.footer ul{list-style:none;font-size:13px;line-height:35px}
.footer ul li:before{content:"› ";color:#fff}
.post{display:flex;gap:16px;margin-bottom:24px}
.post .thumb{width:66px;height:66px;background:linear-gradient(160deg,#8aa3c4,#3c4b66)}
.post .t{font-size:13px;line-height:19px;width:160px}
.post .d{font-size:11px;color:var(--red);margin-top:4px}
.footer .email{left:880px;top:194px;width:240px;height:38px;border:1px solid #555;font-size:11px;color:#999;padding:12px 14px}
.footer .sub-btn{left:880px;top:248px;width:240px;height:38px;background:var(--red);font-size:14px;display:flex;align-items:center;justify-content:center}
.footer .top{left:1152px;top:392px;width:28px;height:28px;border-radius:50%;background:var(--red)}
.footer .copy{left:0;width:1200px;top:446px;text-align:center;font-size:12px}
</style>
</head>
<body>

<div class="abs topbar">
  <div class="abs lang">● &nbsp;&nbsp; English ⌄</div>
  <div class="abs socials"><span><i></i></span><span><i></i></span><span><i></i></span><span><i></i></span><span><i></i></span></div>
</div>

<header class="abs nav">
  <div class="abs brand"><span class="mark"></span><span class="name">TORVA POWER</span></div>
  <nav class="abs menu"><span>RESIDENTIAL</span><span>COMMERCIAL</span><span>OFF-GRID</span><span>CALL US AT: (07) 3000 4182</span></nav>
  <svg class="abs cart" width="22" height="22" viewBox="0 0 22 22"><path d="M2 4h3l2 10h10l2-7H6" fill="none" stroke="#333" stroke-width="1.6"/><circle cx="9" cy="18" r="1.5" fill="#333"/><circle cx="16" cy="18" r="1.5" fill="#333"/><circle cx="17" cy="3" r="5" fill="#c51f2e"/></svg>
  <svg class="abs search" width="14" height="14" viewBox="0 0 14 14"><circle cx="6" cy="6" r="4.5" fill="none" stroke="#333" stroke-width="1.8"/><path d="M9.5 9.5L13 13" stroke="#333" stroke-width="1.8"/></svg>
  <div class="abs quote-btn">GET A QUOTE</div>
</header>

<section class="abs hero" role="img" aria-label="Installer in a hard hat fixing rooftop solar panels under a blue sky"></section>
<h1 class="abs hero-h" style="left:96px;top:324px;font-family:'Oswald',sans-serif;font-weight:600;font-size:54px;line-height:66px;color:#fff">TIRED OF THE POWER BILL<br>GETTING LARGER EACH YEAR?</h1>
<p class="abs" style="left:96px;top:468px;width:590px;font-size:13.5px;line-height:22px;color:#fff">Torva Power is Australia's top provider and authority in solar &amp; off-grid energy solutions. We're here to help you save up to 60% on your energy costs through our effective and efficient energy management systems!</p>
<div class="abs" style="left:96px;top:553px;width:177px;height:40px;background:#fff;color:#333;font-size:13px;display:flex;align-items:center;justify-content:center">PLEASE CLICK HERE</div>

<div class="abs card" style="left:88px">
  <svg width="30" height="80" viewBox="0 0 30 80" fill="none" stroke="#c51f2e" stroke-width="2.4"><path d="M8 2v14M22 2v14M4 16h22v10a11 11 0 0 1-22 0zM15 37v10M15 52c-6 9-8 12-8 16a8 8 0 0 0 16 0c0-4-2-7-8-16z"/></svg>
  <div class="tag">Solar Water Pumps</div><div class="title">Go Solar, Eliminate Fuel Cost</div>
</div>
<div class="abs card active" style="left:351px">
  <svg width="80" height="80" viewBox="0 0 80 80" fill="none" stroke="#fff" stroke-width="2.4"><circle cx="40" cy="26" r="9"/><path d="M40 5v8M40 39v6M19 26h8M53 26h8M25 11l6 6M55 11l-6 6M25 41l6-6M55 41l-6-6M4 62h72M10 52h60M18 52l-3 10M32 52l-2 10M48 52l2 10M62 52l3 10"/></svg>
  <div class="tag">Off Grid Power</div><div class="title">Avoid Blackouts, Go Off-Grid</div>
</div>
<div class="abs card" style="left:614px">
  <svg width="80" height="80" viewBox="0 0 80 80" fill="none" stroke="#c51f2e" stroke-width="2.4"><path d="M44 10L28 40h14l-6 30 18-34H40z"/><path d="M40 2v4M12 14l5 5M68 14l-5 5M4 40h8M68 40h8M12 66l5-5M68 66l-5-5"/></svg>
  <div class="tag">Commercial Solar Power</div><div class="title">Reduce Costs, Grow Your Business</div>
</div>
<div class="abs card" style="left:876px">
  <svg width="80" height="80" viewBox="0 0 80 80" fill="none" stroke="#c51f2e" stroke-width="2.6"><path d="M6 38L40 6l34 32M14 30v40h52V30"/><path d="M33 34v10M47 34v10M28 44h24v6a12 12 0 0 1-24 0zM40 62v8"/></svg>
  <div class="tag">Residential Solar Power</div><div class="title">Save Money For Your Family</div>
</div>

<h2 class="abs head" style="left:88px;top:1164px;font-size:44px;line-height:52px;width:600px">KESTRELWORKS CUT 80% OFF THEIR POWER BILL</h2>
<p class="abs" style="left:90px;top:1276px;width:580px;font-size:13.5px;line-height:22px;color:#8a8a8a">Whether you're a huge commercial establishment or a small property owner, Torva Power has the perfect solution to give you consistent savings on your monthly bills.</p>
<p class="abs" style="left:90px;top:1342px;width:580px;font-size:13.5px;line-height:22px;color:#8a8a8a">Get your FREE Quote and discover how you can save thousands of dollars from reduced energy cost by choosing to go solar!</p>
<div class="abs illus" role="img" aria-label="Illustration of two solar panels and two wind turbines over a dotted world map"></div>

<form class="abs form">
  <h3>Free No Obligation Quote!</h3>
  <div class="sub">Get a FREE customized Quote For your Home or Business!</div>
  <div class="field" style="top:130px">Name</div>
  <div class="field" style="top:185px">Email Address</div>
  <div class="field" style="top:240px">Phone Number</div>
  <div class="field" style="top:295px">Postcode</div>
  <div class="field sel" style="top:350px">Commercial</div>
  <div class="field" style="top:407px;height:106px">Message</div>
  <div class="submit">Get Free Quote</div>
</form>

<h2 class="abs head section-title" style="top:1905px;font-size:44px">TOP RATED PRODUCTS</h2>
<div class="abs prod" style="left:88px"><div class="img" role="img" aria-label="Single solar panel on a pole mount"></div><div class="name">HEADING GOES HERE</div><div class="price">$25.00</div><div class="btn">LEARN MORE</div></div>
<div class="abs prod" style="left:351px"><div class="img" role="img" aria-label="Twin solar panels on a pole mount"></div><div class="name">HEADING GOES HERE</div><div class="price">$25.00</div><div class="btn">LEARN MORE</div></div>
<div class="abs prod" style="left:613px"><div class="img" role="img" aria-label="Solar panels with a home battery unit"></div><div class="name">HEADING GOES HERE</div><div class="price">$25.00</div><div class="btn">LEARN MORE</div></div>
<div class="abs prod" style="left:875px"><div class="img" role="img" aria-label="Solar panel array powering a water pump"></div><div class="name">HEADING GOES HERE</div><div class="price">$25.00</div><div class="btn">LEARN MORE</div></div>

<section class="abs why" role="img" aria-label="Red-tinted background of a brick house"></section>
<h2 class="abs head section-title" style="top:2555px;color:#fff;font-size:42px">WHY DO YOU NEED TO GO SOLAR?</h2>
<div class="abs tabs"><span>Consistent Savings for 20+ Years</span><span>Independent from The Grid</span><span>Increase &amp; Maximise Your Bottomline</span><span>Differentiate Your Business Against Competitors</span><span>Take Part in Solving Global Warming</span></div>
<div class="abs tab-line"></div>
<h3 class="abs head" style="left:88px;top:2746px;font-size:21px;color:#fff">GET CONSISTENT SAVINGS FOR 20+ YEARS</h3>
<p class="abs" style="left:90px;top:2806px;width:520px;font-size:13.5px;line-height:22px;color:#fff">We can't deny that the cost of electricity is consistently rising. And whether you're a commercial organisation or a simple homeowner, dealing with high expensive energy costs can be a real struggle.</p>
<p class="abs" style="left:90px;top:2894px;width:520px;font-size:13.5px;line-height:22px;color:#fff">But what if you can 'game the system' and pay less for your electricity needs? Once installed, our systems can last for 20+ years. Giving you consistent savings for over two decades to come. In addition, you don't need to buy fuels to keep it running and it needs minimal maintenance and repairs. Run your business on solar energy at reduced costs!</p>
<div class="abs" style="left:666px;top:2670px;width:360px;height:400px;border-radius:50%;background:radial-gradient(circle at 50% 25%,#f3c98a 0%,#b98a6a 30%,#3e4f7a 65%,#23335c 100%);box-shadow:14px 8px 0 #a7121d" role="img" aria-label="Solar panel field at sunset"></div>

<h2 class="abs head section-title" style="top:3218px;font-size:42px;line-height:50px">GO SOLAR AND GROW<br>YOUR BUSINESS</h2>
<article class="abs story" style="left:88px">
  <div class="img" role="img" aria-label="City skyline with solar panels in the foreground"></div>
  <h4>A more cost-efficient alternative to your irrigation needs</h4>
  <p>Conventional water pump systems can be quite costly. Volatile prices of fuel and other related expenses...</p>
  <div class="btn">VIEW DETAILS</div>
</article>
<article class="abs story" style="left:611px">
  <div class="img" role="img" aria-label="Rows of solar panels at dusk"></div>
  <h4>Add thousands of dollars to your bottomline!</h4>
  <p>Torva Power has a full range of energy management solutions that will help your business...</p>
  <div class="btn">VIEW DETAILS</div>
</article>

<h2 class="abs head section-title" style="top:3676px;font-size:42px">HERE'S WHAT OUR CLIENTS ARE SAYING</h2>
<div class="abs testi" style="left:100px">
  <div class="avatar" role="img" aria-label="Client portrait"></div>
  <div class="quote" style="left:300px">“</div>
  <p>My new solar water pump hasn't missed a beat and have saved me a fortune in diesel fuel</p>
  <div class="who">Graham</div>
</div>
<div class="abs testi" style="left:652px">
  <div class="avatar" role="img" aria-label="Client portrait"></div>
  <div class="quote" style="left:300px">“</div>
  <p>Have been a pleasure to deal with and came up with a combinations of ideas to save money</p>
  <div class="who">Elise</div>
</div>

<footer class="abs footer">
  <div class="abs f-brand"><span class="mark"></span><span class="name">TORVA POWER</span></div>
  <p class="abs txt" style="left:80px;top:130px;width:300px">Contrary to popular belief, Lorem Ipsum is not simply random text. It has roots in a piece of classical Latin literature.</p>
  <div class="abs" style="left:80px;top:222px;font-size:20px;font-weight:500">(07)3000 4182</div>
  <div class="abs txt" style="left:80px;top:262px;font-size:12px">info@torvapower.com.au</div>
  <div class="abs txt" style="left:80px;top:300px;font-size:12px">48 Wattle Crescent<br>Northgate QLD 4013</div>

  <h5 class="abs" style="left:400px;top:72px">COMPANY</h5>
  <div class="abs bar" style="left:400px;top:98px"></div>
  <ul class="abs" style="left:400px;top:118px"><li>About Us</li><li>Company</li><li>Press &amp; Blog</li><li>Privacy Policy</li><li>Faq</li></ul>

  <h5 class="abs" style="left:612px;top:72px">LATEST POST</h5>
  <div class="abs bar" style="left:612px;top:98px"></div>
  <div class="abs" style="left:612px;top:130px">
    <div class="post"><div class="thumb" role="img" aria-label="House with rooftop solar"></div><div><div class="t">Growth of Clean Energy Part of Solution, Not a Problem</div><div class="d">June 9, 2019</div></div></div>
    <div class="post"><div class="thumb" role="img" aria-label="Worker on a metal roof"></div><div><div class="t">Metal Roofing: The Best for Solar Panels</div><div class="d">January 23, 2019</div></div></div>
  </div>

  <h5 class="abs" style="left:880px;top:72px">OUR NEWSLETTER</h5>
  <div class="abs bar" style="left:880px;top:98px"></div>
  <p class="abs txt" style="left:880px;top:122px;width:240px">Get in your inbox the latest News and Offers from Torva Power</p>
  <div class="abs email">Your email address</div>
  <div class="abs sub-btn">Subscribe</div>
  <svg class="abs top" width="28" height="28" viewBox="0 0 28 28"><path d="M9 16l5-5 5 5" fill="none" stroke="#fff" stroke-width="2"/></svg>
  <div class="abs copy">Copyright © 2019 All Rights Reserved.</div>
</footer>

</body>
</html>
```